Fun conversation piece for the home depicting the history of the ownership (title) and more!

We need some ideas for a framed display to be hung in a home for a new company I started called Ledger of Hearth, LLC. We will create framed (or unframed canvass) wall displays depicting the Ledger of the Hearth (title transfers) with some interesting background on the subdivision the home is located. This will be a conversation piece. Use color if you feel that works best. I am envisioning perhaps the writing to be in old English or old Spanish font to reflect the history of Florida where I am located. I am wanting to incorporate perhaps a picture of the home converted into sketch as a background to the "history". Or we could skip that and use the vegetation (trees) native to the area for a background. I am going to attach something I found online as a sample but I am open to ideas. The sample is a little formal for what I am trying to do. I may sell these framed or as unframed canvass pictures which might need to be a bit more contemporary. I also need a logo if you have any ideas. LH in some form of old English style perhaps? The document attached labeled "Marrowbrook" is an example of the content I will be creating for the picture.
Updates

I misspelled "States" in one of the paragraphs. Can you correct that for me? United States. Not "sates". My bad.

Logo Text

Ledger of Hearth (or LH). Surprise me.

```html
<!DOCTYPE html>
<html lang="en">
<head>
<meta charset="utf-8">
<title>Marrowbrook — Ledger of the Hearth</title>
<link rel="stylesheet" href="https://fonts.googleapis.com/css2?family=Almendra+SC&family=Rye&family=Marcellus&display=swap">
<style>
:root{
  --parchment:#efd9aa;
  --parchment-light:#f6e8c8;
  --paper-edge:#fbf7ee;
  --gold:#b8862f;
  --gold-light:#e2bc68;
  --gold-dark:#6e4a12;
  --ink:#3a2410;
  --ink-soft:#5a3e1e;
  --muted:#8a7a62;
}
*{margin:0;padding:0;box-sizing:border-box}
html,body{width:848px;height:1200px;overflow:hidden;background:var(--paper-edge)}
.poster{
  position:relative;width:848px;height:1200px;overflow:hidden;
  background:radial-gradient(ellipse 62% 58% at 50% 48%,var(--parchment) 0%,var(--parchment) 55%,var(--parchment-light) 80%,var(--paper-edge) 100%);
  color:var(--ink);font-family:"Almendra SC",serif;
}
.home-silhouette{
  position:absolute;left:60px;top:640px;width:520px;height:360px;
  background:radial-gradient(ellipse at 40% 55%,rgba(255,252,244,.75) 0%,rgba(255,252,244,.35) 55%,rgba(255,252,244,0) 80%);
}
.frame{position:absolute;inset:0}
.corner-flourish{
  position:absolute;width:120px;height:120px;
  background:radial-gradient(circle at var(--cx) var(--cy),rgba(184,134,47,.55) 0%,rgba(184,134,47,.2) 45%,rgba(184,134,47,0) 75%);
}
.corner-flourish.tl{left:34px;top:22px;--cx:20%;--cy:20%}
.corner-flourish.tr{right:34px;top:22px;--cx:80%;--cy:20%}
.corner-flourish.bl{left:34px;bottom:28px;--cx:20%;--cy:80%}
.corner-flourish.br{right:34px;bottom:28px;--cx:80%;--cy:80%}
.scroll-ornament{
  position:absolute;left:260px;width:328px;
  background:radial-gradient(ellipse at 50% 50%,rgba(184,134,47,.45) 0%,rgba(184,134,47,.15) 55%,rgba(184,134,47,0) 80%);
}
.scroll-ornament.top{top:110px;height:64px}
.scroll-ornament.bottom{top:332px;height:52px}
.series-label{
  position:absolute;left:326px;top:73px;width:198px;height:28px;
  font-family:"Marcellus",serif;font-size:16px;color:var(--ink-soft);
  text-align:center;line-height:28px;letter-spacing:.3px;
}
.neighborhood-title{
  position:absolute;left:165px;top:196px;width:518px;text-align:center;
  font-family:"Rye",serif;font-size:58px;letter-spacing:1px;color:var(--gold-light);
  text-shadow:1px 1px 0 var(--gold),2px 2px 0 var(--gold),3px 3px 0 var(--gold-dark),4px 4px 0 var(--gold-dark),5px 6px 4px rgba(60,36,10,.45);
}
.year-span{
  position:absolute;left:330px;top:383px;width:190px;text-align:center;
  font-family:"Marcellus",serif;font-size:19px;letter-spacing:2px;color:var(--muted);
}
.neighborhood-history{
  position:absolute;left:86px;top:458px;width:678px;
  font-size:9.4px;line-height:13.6px;text-align:justify;color:var(--ink);
}
.neighborhood-history p{text-align-last:left}
.neighborhood-history p.centered-last{text-align-last:center}
.section-heading{
  position:absolute;left:0;top:650px;width:848px;text-align:center;
  font-size:37px;letter-spacing:1px;color:var(--ink);font-weight:700;
}
.title-ledger{position:absolute;left:86px;top:726px;width:680px;list-style:none}
.title-ledger li{display:flex;height:28.6px;align-items:center;font-size:17px;color:var(--ink)}
.title-ledger .date{width:190px;flex:none;letter-spacing:.3px}
.title-ledger .owner{flex:1;text-align:center;letter-spacing:.3px}
.presenter{position:absolute;left:0;top:1002px;width:848px;text-align:center;color:var(--ink)}
.presenter .presented-by{font-size:13px;font-weight:700}
.presenter .mark{display:block;width:34px;height:34px;margin:8px auto 10px;border:1.5px solid var(--ink-soft)}
.presenter .company{font-size:12px;letter-spacing:.5px}
</style>
</head>
<body>
<main class="poster">
  <div class="home-silhouette" role="img" aria-label="Faint pale silhouette of a tree and the house behind the ownership ledger"></div>

  <svg class="frame" width="848" height="1200" viewBox="0 0 848 1200" aria-hidden="true">
    <rect x="42" y="30" width="764" height="1132" fill="none" stroke="var(--gold)" stroke-width="2.5"/>
    <rect x="54" y="43" width="740" height="1106" fill="none" stroke="var(--gold)" stroke-width="1.5"/>
    <rect x="326" y="73" width="198" height="28" rx="3" fill="none" stroke="var(--gold-dark)" stroke-width="2"/>
    <line x1="300" y1="104" x2="550" y2="104" stroke="var(--gold)" stroke-width="1.5"/>
    <rect x="165" y="180" width="518" height="152" rx="76" fill="none" stroke="var(--gold)" stroke-width="4"/>
    <rect x="180" y="192" width="488" height="128" rx="64" fill="none" stroke="var(--gold-dark)" stroke-width="1.5"/>
    <line x1="330" y1="413" x2="520" y2="413" stroke="var(--gold)" stroke-width="2"/>
    <circle cx="326" cy="413" r="3" fill="var(--gold)"/>
    <circle cx="524" cy="413" r="3" fill="var(--gold)"/>
  </svg>

  <div class="corner-flourish tl" role="img" aria-label="Gold scrollwork flourish"></div>
  <div class="corner-flourish tr" role="img" aria-label="Gold scrollwork flourish"></div>
  <div class="corner-flourish bl" role="img" aria-label="Gold scrollwork flourish"></div>
  <div class="corner-flourish br" role="img" aria-label="Gold scrollwork flourish"></div>
  <div class="scroll-ornament top" role="img" aria-label="Gold scrollwork crest above the title cartouche"></div>
  <div class="scroll-ornament bottom" role="img" aria-label="Gold scrollwork below the title cartouche"></div>

  <div class="series-label">Ledger of Hearth</div>
  <h1 class="neighborhood-title">Marrowbrook</h1>
  <div class="year-span">1835 - 2020</div>

  <section class="neighborhood-history">
    <p>Marrowbrook is a neighborhood in the City of Bellhaven. Located east of Cedar Terrace, Marrowbrook is bordered by 9th Avenue to the west and 12th Avenue and Millwright's Creek to the east. Initially developed in 1954, an addition was added in 1956. It is located in a</p>
    <p class="centered-last">beautiful area of America's 1st Settlement (1559), Bellhaven, Florida encompassed with towering pine trees and breathtaking heritage oaks.</p>
    <p>The land comprising Marrowbrook was originally owned by Tomas Arrieta under a Spanish Land Grant and affirmed by President Silas Whitcombe on September 7, 1835. Spain relinquished Florida to the United States in 1819 under the Harlow-Ortega Treaty and lands previously granted to settlers prior thereto were honored if claims were filed and approved by the United States government.</p>
    <p class="centered-last">Through the years, the land changed hands many times but was eventually developed into the Marrowbrook subdivision in 1954, by Warren Ashby, President of Marrowbrook, Inc. The subdivision contains 63 lots with a beautiful, oak-filled park located just off of Halden Street. Built in 1957 and containing approximately 2606 square feet of living, garage and patio space, the home located at 417 Lantana Street is a trip back in time to when houses were carefully planned catering to modern sensibilities, neither too big nor too small, neither too formal nor too casual.</p>
  </section>

  <h2 class="section-heading">Ledger of Hearth</h2>

  <ol class="title-ledger">
    <li><span class="date">September 9, 1835</span><span class="owner">Tomas Arrieta, Spanish Land Grant</span></li>
    <li><span class="date">April 27, 1954</span><span class="owner">Marrowbrook Plat approved by Alder County</span></li>
    <li><span class="date">April 29, 1957</span><span class="owner">Warren Ashby, III and Louise M. Ashby</span></li>
    <li><span class="date">September 20, 1960</span><span class="owner">Ada Ruth Keller (Dunmore)</span></li>
    <li><span class="date">February 11, 1966</span><span class="owner">Harold P. Lindqvist and Marian J. Lindqvist</span></li>
    <li><span class="date">January 20, 1995</span><span class="owner">Daniel R. Whitford</span></li>
    <li><span class="date">September 1, 2020</span><span class="owner">Daniel R. Whitford and Martin Everett Hale</span></li>
  </ol>

  <footer class="presenter">
    <div class="presented-by">Presented by</div>
    <span class="mark" aria-hidden="true"></span>
    <div class="company">Ledger of Hearth, LLC</div>
  </footer>
</main>
</body>
</html>
```